Texas Marsh Reed Conservation League

We need to design the home page of this new website. We would like a fun website design for provides as a resource for members and information for potential members.
Please design so that we can see a portion of background on each side on the website.
I just need the final design files psd no coding needed.
Attached is their logo (colors are not 100% set in stone either so can mess with those as I did in the quick mockup attached)
Attached is a pdf newsletter they send out, you can get a feel for them and what they are about. The design is crappy and we are here to fix that going forward and we are starting with the website.
Here are some quick example websites (design style is open)
- I attached a quick mockup i did just for a content visual but by all means do what you want.
- http://www.lonestarbizladies.org/
- http://www.wqrtf.org/
- http://demo.webkitpalette.com/demo.php?cat=html5themes&host=layoutbazaar&temp=veltrona
- http://www.fieldkeep.org/
- http://www.urbanpantry.org/
- http://www.projectcozy.org/
here are some of the other chapters website (pretty bad!)
and here are some of the others:
- http://www.kdwrcl.org/
- http://wrcl.org/
- http://www.gwrcl.org/
Content Items that need to be included:
1. Logo
2. Menu - home, about, members, resources, events, membership, contact
3. Become a member - button or action
4. social links - facebook, linkedin, youtube
5. banner - that needs to explain their purpose "Promoting environmental stewardship through operations, research, education and outreach" (or this can be worked into the design)
6. Upcoming event (s)
7. Advertisement - members can place an ad on the website, this can be a placeholder for now
8. newsletter signup
9. advertise with us - this link can be in the footer
30-60 years of age, succesfull (household budgets of 120K+ men and women that live in texas.
Education

```html
<!DOCTYPE html>
<html lang="en">
<head>
<meta charset="utf-8">
<title>Texas Marsh Reed Conservation League — Home</title>
<link rel="stylesheet" href="https://fonts.googleapis.com/css2?family=Arimo:wght@400;700&family=Fjalla+One&family=Aldrich&family=Open+Sans:ital,wght@0,400;0,700;1,400&display=swap">
<style>
:root{
  --navy:#0f3a86;
  --navy-dark:#0a2c6a;
  --red:#d9465a;
  --red-dark:#b8344a;
  --ink:#333;
  --paper:#dcdcdc;
  --field:#e3e3e3;
  --footer:#343434;
  --white:#fff;
}
*{margin:0;padding:0;box-sizing:border-box}
html,body{width:970px;height:1200px;overflow:hidden;background:var(--white)}
body{position:relative;font-family:Arimo,Arial,sans-serif;color:var(--ink)}
.abs{position:absolute}

.backdrop{left:0;top:0;width:970px;height:420px;
  background:linear-gradient(180deg,#5f95cf 0%,#a9cbe9 22%,#dfeaf3 38%,#9db985 52%,#c7d2c9 68%,#fff 100%)}
.topline{left:0;top:0;width:970px;height:6px;background:var(--navy)}
.account{left:694px;top:6px;width:194px;height:30px;background:var(--navy);border:1px solid #fff;border-top:0;border-radius:0 0 4px 4px;
  color:#fff;font-size:16px;text-align:center;line-height:28px}

.brand{left:81px;top:36px;width:175px}
.brand-name{font-family:Aldrich,sans-serif;font-size:40px;color:var(--navy);letter-spacing:1px;line-height:44px;display:flex;align-items:center;gap:8px}
.brand-name i{display:inline-block;width:12px;height:12px;background:var(--red);border-radius:50%}
.brand-tag{font-family:Arimo,sans-serif;font-size:7px;font-weight:700;color:#111;margin-top:6px;white-space:nowrap}

.social{left:729px;top:69px;display:flex;gap:11px}
.social span{width:28px;height:28px;border-radius:50%;background:var(--navy)}
.social span:nth-child(2){background:#c8373a}
.social span:nth-child(3){background:#3ba8dc}
.social span:nth-child(4){background:#e2632a}

.nav{left:81px;top:133px;width:807px;height:35px;background:var(--red);display:flex;align-items:center;padding-left:19px;
  color:#fff;font-weight:700;font-size:11.5px}
.nav .sep{margin:0 20px;font-weight:400}
.nav svg{display:block}

.hero{left:81px;top:168px;width:808px;height:360px;
  background:radial-gradient(ellipse at 50% 85%,#b7c84f 0%,#7e9a3a 30%,transparent 60%),
  linear-gradient(180deg,#4d7a2e 0%,#6a8f3c 20%,#8a8a6c 30%,#5d5a47 55%,#8ea04a 100%)}
.hero-title{left:81px;top:340px;width:808px;text-align:center;padding-left:84px;font-family:"Fjalla One",sans-serif;font-size:31px;color:#fff;letter-spacing:.5px;text-shadow:0 2px 3px rgba(0,0,0,.6)}
.hero-sub{left:81px;top:376px;width:808px;text-align:center;padding-left:84px;font-size:19.5px;color:#fff;text-shadow:0 1px 3px rgba(0,0,0,.8)}
.join{left:673px;top:429px;width:216px;height:39px;background:var(--red);clip-path:polygon(14px 0,100% 0,100% 100%,0 100%);
  color:#fff;font-family:"Open Sans",sans-serif;font-weight:700;font-size:19px;line-height:39px;text-align:right;padding-right:10px}

.features{left:81px;top:528px;width:808px;height:248px;background:linear-gradient(180deg,var(--paper) 0%,#e2e2e2 100%)}
.features .band{position:absolute;left:0;right:0;top:131px;bottom:0;background:linear-gradient(180deg,#c8394f 0%,var(--red) 40%,#c13a50 100%);border-radius:0 0 4px 4px}
.card{top:544px;width:227px;height:187px;border:2px solid #fff;background:#121212}
.card-title{height:42px;background:#d7d7d7;text-align:center;font-size:18px;line-height:42px;color:#444;letter-spacing:.5px}
.card-media{margin:6px 6px 0;height:98px;background:linear-gradient(180deg,#3e6f24 0%,#79a64a 50%,#6d9a43 100%)}
.card-btn{position:absolute;left:53px;bottom:-12px;width:110px;height:27px;background:var(--navy);border:1px solid #5b7fc0;
  color:#fff;font-size:15px;font-weight:700;text-align:center;line-height:25px}

.about-title{left:81px;top:802px;font-family:Aldrich,sans-serif;font-weight:400;font-size:23px;color:#333}
.about-text{left:82px;top:838px;width:520px;font-size:10.5px;line-height:17.8px;color:#333}
.about-text p+p{margin-top:17.8px}
.more{left:78px;top:993px;font-family:"Open Sans",sans-serif;font-style:italic;font-size:9px;color:#3565b0}

.news-title{left:653px;top:792px;font-family:Aldrich,sans-serif;font-weight:400;font-size:23px;color:#333}
.field{left:653px;width:234px;background:var(--field);border-radius:3px;font-size:9.5px;color:#888;padding:9px 8px}
.send{left:807px;top:990px;width:79px;height:27px;background:var(--red);border-radius:3px;color:#fff;font-size:17px;text-align:center;line-height:27px}

.footer{left:0;top:1043px;width:970px;height:157px;background:var(--footer)}
.advert{left:323px;top:1057px;width:287px;height:34px;border-radius:5px;background:#555;overflow:hidden}
.advert-label{position:absolute;left:24px;top:0;line-height:34px;font-family:"Open Sans",sans-serif;font-weight:700;font-size:15px;color:#e8e8e8;letter-spacing:.5px}
.advert-cta{position:absolute;right:0;top:0;width:75px;height:34px;background:var(--red);clip-path:polygon(8px 0,100% 0,100% 100%,8px 100%,0 50%);
  color:#fff;font-size:7.5px;font-weight:700;text-decoration:underline;text-align:center;line-height:34px}
.rule{left:115px;top:1106px;width:735px;height:2px;background:#111;border-bottom:1px solid #555}
.foot-brand{left:105px;top:1122px;color:#ddd}
.foot-brand .brand-name{font-size:26px;color:#ddd;line-height:30px}
.foot-brand .brand-tag{color:#ddd;font-size:5px;margin-top:3px}
.foot-nav{left:235px;top:1139px;font-size:10.5px;color:#fff;white-space:nowrap}
.foot-nav .sep{margin:0 10px}
.foot-social{left:739px;top:1136px;display:flex;gap:3px}
.foot-social span{width:23px;height:23px;border-radius:50%;background:#fff;border:2px solid #ccc}
.copyright{left:379px;top:1164px;font-size:10.5px;color:#ccc}
</style>
</head>
<body>
<div class="abs backdrop" role="img" aria-label="Sky and lakeside trees fading into the page background"></div>
<div class="abs topline"></div>
<div class="abs account">Login&nbsp; / &nbsp;Register</div>

<div class="abs brand">
  <div class="brand-name"><i></i>TMRCL</div>
  <div class="brand-tag">Texas Marsh Reed Conservation League</div>
</div>

<div class="abs social" aria-label="Social links"><span></span><span></span><span></span><span></span></div>

<nav class="abs nav">
  <svg width="19" height="16" viewBox="0 0 19 16" aria-label="Home"><path d="M9.5 1 1 8h2.5v7h4.5v-4.5h3V15h4.5V8H18z" fill="#24408a"/></svg>
  <span class="sep">|</span>ABOUT<span class="sep">|</span>MEMBERS<span class="sep">|</span>RESOURCES<span class="sep">|</span>EVENTS<span class="sep">|</span>MEMBERSHIP<span class="sep">|</span>CONTACT
</nav>

<div class="abs hero" role="img" aria-label="Photograph of a pond covered with water lily pads and a tree-lined shore"></div>
<div class="abs hero-title">PROMOTING ENVIRONMENTAL STEWARDSHIP</div>
<div class="abs hero-sub">Through Opertation , Research Education and Outreach</div>
<div class="abs join">BECOME A MEMBER</div>

<section class="abs features"><div class="band"></div></section>
<div class="abs card" style="left:119px">
  <div class="card-title">RESOURCES</div>
  <div class="card-media" role="img" aria-label="Photograph of a purple water lily among reeds"></div>
  <div class="card-btn">more Info</div>
</div>
<div class="abs card" style="left:373px">
  <div class="card-title">EVENTS</div>
  <div class="card-media" role="img" aria-label="Photograph of a purple water lily among reeds"></div>
  <div class="card-btn">more Info</div>
</div>
<div class="abs card" style="left:627px">
  <div class="card-title">ADVERTISEMENT</div>
  <div class="card-media" role="img" aria-label="Photograph of a purple water lily among reeds"></div>
  <div class="card-btn">more Info</div>
</div>

<h2 class="abs about-title">About TMRCL</h2>
<div class="abs about-text">
  <p>simply dummy text of the printing and typesetting industry. Lorem Ipsum has been the industry's standard dummy text ever since the 1500s, when an unknown printer took a galley of type and scrambled it to make a type specimen book. It has survived not only five centuries, but also the leap into electronic typesetting, remaining essentially unchanged.</p>
  <p>It was popularised in the 1960s with the release of Transfix sheets containing Lorem Ipsum passages, and more recently with desktop publishing software like Quill LayoutPro including versions of Lorem Ipsum.</p>
</div>
<div class="abs more">More Details ››</div>

<h2 class="abs news-title">Newsletter Sign up</h2>
<div class="abs field" style="top:835px;height:27px">Name</div>
<div class="abs field" style="top:873px;height:27px">Email</div>
<div class="abs field" style="top:912px;height:64px">Massage</div>
<div class="abs send">Send</div>

<footer class="abs footer"></footer>
<div class="abs advert"><span class="advert-label">ADVERTISE WITH US</span><span class="advert-cta">Click Here</span></div>
<div class="abs rule"></div>
<div class="abs foot-brand">
  <div class="brand-name">TMRCL</div>
  <div class="brand-tag">Texas Marsh Reed Conservation League</div>
</div>
<div class="abs foot-nav">HOME<span class="sep">|</span>ABOUT<span class="sep">|</span>MEMBERS<span class="sep">|</span>RESOURCES<span class="sep">|</span>EVENTS<span class="sep">|</span>MEMBERSHIP<span class="sep">|</span>CONTACT</div>
<div class="abs foot-social" aria-label="Social links"><span></span><span></span><span></span><span></span></div>
<div class="abs copyright">©&nbsp; 2014 | TMRCL All Right Reserved</div>
</body>
</html>
```